Etiketten-Design für Kaffeetüten
Zielgruppe
Wir stellen eine nachhaltige alternative zu herkömmlichem Bohnenkaffee her.
Regional, nachhaltig und koffeinfrei.
Hierzu verwenden wir Süßlupinen die wir von einem Partnerbauern aus Niedersachsen beziehen. Diese Lupinen werden wie herkömmlicher Kaffee in einem Trommelröster geröstet und anschließend gemahlen.
Unser Lupinenkaffee kann wie herkömmlicher Kaffee im Filter in der Frenchpress oder in einem Espressokocher zubereitet werden.
Wir bieten unseren Kunden zwei verschiedene Sorten an, eine 'Mild' und eine 'Klassisch'.
Die Zielgruppe sind ernährungsbewusste Menschen die gezielt eine alternative zu herkömmlichen Bohnenkaffee suchen. (Koffeinfreier Kaffee, Getreidekaffee)
Aufgabenstellung
Wir möchten ein modernes Design des Etiketts, das den Stil des Logos widerspiegelt. Die beiden Sorten 'Mild' und 'Klassisch' sollten gut von einander zu unterscheiden sein.
Es gibt ein Etikett für die Vorderseite, hier soll die Produktbezeichnung 'Lupinenkaffee' sowie die Mengenangabe '500g' stehen.
Ggf. 3 Icons für mögliche Brühmethoden (Filter, Frenchpress, Espressokocher)
Auf dem Etikett der Rückseite müssen zum einen die Zutaten, die Zubereitung sowie die Nährwertangaben (in TabellenForm) angegeben werden. Sowie ein EAN Code die Herstellerangaben und die Adresse der Homepage.
FENNO BREW – Deine nachhaltige Kaffeealternative
Zutaten: weiße Süßlupinen, geröstet
Zubereitung: Du kannst Deinen Lupinenkaffee mit der French Press, dem klassischen Filter oder dem Espressokocher zubereiten. Für den optimalen Geschmack empfehlen wir 8g Kaffeepulver für 100ml.
Hersteller:
FENNO GmbH
Birkenhainer Weg 57
40213 Düsseldorf
www.FENNOBREW.de
 Nährwertangaben für 100 ml Kaffee
Energie 12kj - 5 kcal
Fett <0,1g
Davon gesättigt <0,1g
Kohlenhydrate <1,0g
Davon Zucker <0,05g
Eiweiß <1,0g
Salz <0,05g
Die Kaffeetüte, auf die das Etikett geklebt wird, ist in einer braunen Kartonfarbe.
Das Etikett für die Kaffeetüten hat die Maße 7x11.
Das Logo hat die Schriftart 'Cera'. Die verwendete Schriftart sollte möglichst gleich sein, oder gut damit harmonieren.

```html
<!DOCTYPE html>
<html lang="de">
<head>
<meta charset="utf-8">
<title>FENNO BREW – Lupinenkaffee Etiketten</title>
<link rel="stylesheet" href="https://fonts.googleapis.com/css2?family=Jost:wght@400;500&display=swap">
<style>
  :root {
    --canvas: #f4f1ec;
    --label-dark: #1d1e1e;
    --variant-classic: #5094a5;
    --variant-mild: #c2962a;
    --ink: #161616;
  }
  html, body {
    margin: 0;
    width: 1200px;
    height: 1200px;
    overflow: hidden;
    background: var(--canvas);
    font-family: "Jost", "Futura", sans-serif;
  }
  .stage {
    position: relative;
    width: 1200px;
    height: 1200px;
  }
  .label {
    position: absolute;
    top: 255px;
    width: 440px;
    height: 691px;
    overflow: hidden;
  }
  .label--classic { left: 110px; --accent: var(--variant-classic); }
  .label--mild { left: 650px; --accent: var(--variant-mild); }

  .label__bg { position: absolute; inset: 0; }

  .brand {
    position: absolute;
    top: 40px;
    left: 0;
    right: 0;
    display: flex;
    flex-direction: column;
    align-items: center;
  }
  .brand__ring {
    width: 180px;
    height: 180px;
    border: 3px solid var(--accent);
    border-radius: 50%;
    box-sizing: border-box;
  }
  .brand__name {
    margin-top: 48px;
    color: var(--accent);
    font-weight: 500;
    font-size: 38px;
    letter-spacing: 0.22em;
    padding-left: 0.22em;
    line-height: 1;
  }

  .product {
    position: absolute;
    top: 398px;
    left: 0;
    right: 0;
    text-align: center;
    color: var(--ink);
  }
  .product__line {
    display: block;
    font-weight: 400;
    font-size: 64px;
    line-height: 1;
    letter-spacing: 0.03em;
  }
  .product__rule {
    width: 280px;
    height: 2px;
    margin: 8px auto 12px;
    background: var(--ink);
  }
  .product__variant {
    margin-top: 12px;
    font-size: 23px;
    letter-spacing: 0.02em;
  }

  .brew-methods {
    position: absolute;
    top: 605px;
    left: 118px;
    display: flex;
    gap: 38px;
  }
  .brew-methods svg { width: 50px; height: 58px; }

  .weight {
    position: absolute;
    top: 622px;
    right: 24px;
    font-size: 24px;
    color: var(--ink);
  }
</style>
</head>
<body>
<main class="stage">

  <section class="label label--classic">
    <svg class="label__bg" viewBox="0 0 440 691" aria-hidden="true">
      <rect width="440" height="691" fill="var(--variant-classic)"/>
      <path d="M0 0H440V272C350 350 200 395 0 373Z" fill="var(--label-dark)"/>
    </svg>
    <div class="brand">
      <div class="brand__ring"></div>
      <div class="brand__name">FENNO BREW</div>
    </div>
    <div class="product">
      <span class="product__line">LUPINEN</span>
      <div class="product__rule"></div>
      <span class="product__line">KAFFEE</span>
      <div class="product__variant">Klassisch</div>
    </div>
    <div class="brew-methods">
      <svg viewBox="0 0 50 58" aria-label="French Press"><g fill="none" stroke="#161616" stroke-width="3"><path d="M21 4h8M25 4v10M12 14h26M14 14v38h22V14M36 22h6v18h-6M10 54h30"/></g><rect x="17" y="32" width="16" height="17" fill="#161616"/></svg>
      <svg viewBox="0 0 50 58" aria-label="Filter"><g fill="none" stroke="#161616" stroke-width="3"><path d="M4 14h42L29 36h-8ZM8 8h34"/><path d="M25 42c-3 5-3 9 0 9s3-4 0-9Z"/></g></svg>
      <svg viewBox="0 0 50 58" aria-label="Espressokocher"><g fill="none" stroke="#161616" stroke-width="3"><path d="M16 6h18l3 22H13ZM13 28h24l-4 26H17ZM37 10h7v14h-6"/></g><rect x="20" y="34" width="10" height="16" fill="#161616"/></svg>
    </div>
    <div class="weight">500g</div>
  </section>

  <section class="label label--mild">
    <svg class="label__bg" viewBox="0 0 440 691" aria-hidden="true">
      <rect width="440" height="691" fill="var(--variant-mild)"/>
      <path d="M0 0H440V272C350 350 200 395 0 373Z" fill="var(--label-dark)"/>
    </svg>
    <div class="brand">
      <div class="brand__ring"></div>
      <div class="brand__name">FENNO BREW</div>
    </div>
    <div class="product">
      <span class="product__line">LUPINEN</span>
      <div class="product__rule"></div>
      <span class="product__line">KAFFEE</span>
      <div class="product__variant">Mild</div>
    </div>
    <div class="brew-methods">
      <svg viewBox="0 0 50 58" aria-label="French Press"><g fill="none" stroke="#161616" stroke-width="3"><path d="M21 4h8M25 4v10M12 14h26M14 14v38h22V14M36 22h6v18h-6M10 54h30"/></g><rect x="17" y="32" width="16" height="17" fill="#161616"/></svg>
      <svg viewBox="0 0 50 58" aria-label="Filter"><g fill="none" stroke="#161616" stroke-width="3"><path d="M4 14h42L29 36h-8ZM8 8h34"/><path d="M25 42c-3 5-3 9 0 9s3-4 0-9Z"/></g></svg>
      <svg viewBox="0 0 50 58" aria-label="Espressokocher"><g fill="none" stroke="#161616" stroke-width="3"><path d="M16 6h18l3 22H13ZM13 28h24l-4 26H17ZM37 10h7v14h-6"/></g><rect x="20" y="34" width="10" height="16" fill="#161616"/></svg>
    </div>
    <div class="weight">500g</div>
  </section>

</main>
</body>
</html>
```